Billboard to promote Harlow County, NC

I would like a billboard designed for the Chamber of Commerce. The size of the board is 10'h by 24'w. I would like our logo colors used and IF space permits, include our logo. I want to board to be very easy to read with a simplistic message of #StayWithHarlow, Invest in this community, Shop, Dine, Live. I would like our web address to scroll the bottom of the board, www.TheHarlowChamber.example

Target Market(s)

Local residents and visitors

Industry/Entity Type

Chamber Of Commerce

Requirements
Must have
• Quick message
• Easy to read
• Bold type
Nice to have
• Our logo, if space permits.
Should not have
• Should not be too busy or hard to read. People are driving by at 55-65 miles per hour.

```html
<!DOCTYPE html>
<html lang="en">
<head>
<meta charset="utf-8">
<title>#StayWithHarlow Billboard – Harlow Chamber of Commerce &amp; Tourism</title>
<link rel="stylesheet" href="https://fonts.googleapis.com/css2?family=Montserrat:wght@700;800&display=swap">
<style>
  :root {
    --navy-deep: #06225f;
    --navy: #0b3a8f;
    --blue-bright: #1f76d6;
    --blue-text: #0c5cc6;
    --orange: #f7941d;
    --orange-shade: #d77a12;
    --white: #ffffff;
    --paper: #f1f2f4;
    --paper-shade: #b9bec6;
    --logo-ink: #123d8c;
  }
  * { margin: 0; padding: 0; box-sizing: border-box; }
  html, body {
    width: 1200px;
    height: 500px;
    overflow: hidden;
    background: var(--white);
  }
  .billboard {
    display: block;
    width: 1200px;
    height: 500px;
    font-family: "Montserrat", Arial, sans-serif;
  }
  .hashtag {
    fill: var(--orange);
    font-weight: 800;
    font-size: 82px;
  }
  .band-text {
    fill: var(--blue-text);
    font-weight: 800;
    font-size: 74px;
  }
  .pillars {
    fill: var(--white);
    font-weight: 700;
    font-size: 82px;
  }
  .web-address {
    fill: var(--orange);
    font-weight: 700;
    font-size: 22px;
  }
  .chamber-name {
    fill: var(--logo-ink);
    font-weight: 700;
    font-size: 10.5px;
  }
  .chamber-mark { fill: var(--logo-ink); }
</style>
</head>
<body>
<svg class="billboard" viewBox="0 0 1200 500" xmlns="http://www.w3.org/2000/svg" aria-labelledby="board-title">
  <title id="board-title">#StayWithHarlow – Invest in this community. Shop. Dine. Live. www.TheHarlowChamber.example</title>
  <defs>
    <radialGradient id="sky" cx="0.18" cy="0.45" r="1.05">
      <stop offset="0" stop-color="var(--blue-bright)"/>
      <stop offset="0.55" stop-color="var(--navy)"/>
      <stop offset="1" stop-color="var(--navy-deep)"/>
    </radialGradient>
    <linearGradient id="spokesperson-tones" x1="0" y1="0" x2="1" y2="1">
      <stop offset="0" stop-color="#3a4a66"/>
      <stop offset="0.5" stop-color="#c9a48c"/>
      <stop offset="1" stop-color="#e7e9ee"/>
    </linearGradient>
    <linearGradient id="curl" x1="0" y1="0" x2="1" y2="1">
      <stop offset="0" stop-color="var(--paper-shade)"/>
      <stop offset="0.6" stop-color="var(--paper)"/>
      <stop offset="1" stop-color="var(--white)"/>
    </linearGradient>
  </defs>

  <!-- background -->
  <rect class="backdrop" width="1200" height="500" fill="url(#sky)"/>

  <!-- slanted message band -->
  <polygon class="band-shadow" points="0,372 1200,270 1200,290 0,398" fill="var(--orange-shade)"/>
  <polygon class="band" points="0,262 1200,160 1200,270 0,372" fill="var(--orange)"/>

  <!-- spokesperson photograph area -->
  <rect class="spokesperson-photo" x="0" y="28" width="300" height="230" fill="url(#spokesperson-tones)"
        role="img" aria-label="Photo of a businessman shouting into an orange and white megaphone"/>

  <!-- headline -->
  <text class="hashtag" x="322" y="138" textLength="822" lengthAdjust="spacingAndGlyphs">#StayWithHarlow</text>

  <text class="band-text" x="80" y="337" textLength="1060" lengthAdjust="spacingAndGlyphs"
        transform="rotate(-4.86 80 337)">INVEST IN THIS COMMUNITY</text>

  <text class="pillars" x="300" y="428" textLength="788" lengthAdjust="spacingAndGlyphs">SHOP . DINE . LIVE</text>

  <text class="web-address" x="684" y="466" textLength="468" lengthAdjust="spacingAndGlyphs">WWW.THEHARLOWCHAMBER.EXAMPLE</text>

  <!-- page curl corner -->
  <polygon class="corner-reveal" points="0,330 0,500 200,500" fill="var(--white)"/>
  <path class="corner-flap" d="M0,330 C70,372 140,425 200,500 C150,470 90,455 22,452 Z" fill="url(#curl)"/>

  <!-- chamber name -->
  <g class="chamber-signature">
    <circle class="chamber-mark" cx="74" cy="432" r="9"/>
    <text class="chamber-name" x="18" y="458">HARLOW CHAMBER</text>
    <text class="chamber-name" x="18" y="471">OF COMMERCE &amp; TOURISM</text>
  </g>
</svg>
</body>
</html>
```